Professional and Modern Company Letterhead for Fintech Startup

Brisk lending is a fintech startup that provides home financing.

Our company requires letterhead in Microsoft word format. Colors must come from our ADA compliant doc.

Company logo, equal housing opportunity logo, and legal language must be included somewhere on the document.

We'd love an option that maximizes space on the page for text vs have design take up the entire thing.

Target Market(s)

Partners, clients, and employees

Industry/Entity Type

Finance

Font styles to use
Sans Serif

Requirements
Must have
• Must use company colors that are ADA compliant (see attachment). Must include logo in a prominent position. Must include equal housing opportunity logo and legal info at the bottom:

©Brisk Lending LLC. NMLS #5093374 | 4716 Harlow Avenue #204, Boulder, CO 80305 | Not available in all states | 800.437.5068 | help@brisklending-example.com
Nice to have
• Something modern and clean.

```html
<!DOCTYPE html>
<html lang="en">
<head>
<meta charset="utf-8">
<title>Brisk lending — Letterhead</title>
<link rel="stylesheet" href="https://fonts.googleapis.com/css2?family=Open+Sans:wght@400;600&family=Roboto:wght@400&display=swap">
<style>
  :root {
    --backdrop: #dedede;
    --paper: #f8f8f8;
    --teal: #58b3bf;
    --navy: #0d1f3c;
    --ink: #474747;
    --ink-soft: #555555;
    --mark: #111111;
    --signature-tone: #d9d9d9;
    --white: #ffffff;
  }
  * { box-sizing: border-box; margin: 0; padding: 0; }
  html, body {
    width: 1153px; height: 1200px; overflow: hidden;
    background: var(--backdrop);
  }
  .letterhead {
    position: absolute; left: 175px; top: 40px;
    width: 803px; height: 1120px;
    background: var(--paper);
    box-shadow: 0 6px 24px rgba(0,0,0,0.12);
    font-family: "Open Sans", sans-serif;
    color: var(--ink);
  }
  .brand {
    position: absolute; left: 72px; top: 112px;
    display: flex; align-items: center; gap: 10px;
    font-family: "Open Sans", sans-serif;
    font-weight: 600; font-size: 38px; line-height: 1;
    color: var(--teal);
  }
  .brand-square { width: 14px; height: 14px; background: var(--teal); }
  .company-details {
    position: absolute; right: 66px; top: 84px;
    font-family: "Roboto", sans-serif; font-size: 13.5px; line-height: 16.8px;
    font-style: normal;
    color: var(--ink-soft);
  }
  .company-details .legal { margin-bottom: 5px; }
  .contact-line { display: flex; align-items: center; gap: 5px; line-height: 18px; }
  .contact-line svg { width: 12px; height: 12px; flex: none; }
  .letter-body {
    position: absolute; left: 72px; top: 262px; width: 659px;
    font-size: 14.4px; line-height: 21.6px;
  }
  .letter-body p { margin-bottom: 21.6px; text-align: justify; }
  .letter-body .salutation { text-align: left; }
  .signature {
    position: absolute; left: 73px; top: 829px;
    width: 94px; height: 86px;
    background: var(--signature-tone); opacity: 0.5;
  }
  .housing-badge {
    position: absolute; left: 646px; top: 976px; width: 106px; height: 102px;
  }
  .footer-band { position: absolute; left: 0; bottom: 0; width: 803px; height: 27px; }
  .website {
    position: absolute; right: 24px; bottom: 0; height: 27px;
    display: flex; align-items: center;
    font-family: "Roboto", sans-serif; font-size: 15.5px; line-height: 1;
    color: var(--white); white-space: nowrap;
  }
</style>
</head>
<body>
<main class="letterhead">
  <header>
    <div class="brand"><span class="brand-square"></span><span class="brand-name">Brisk lending</span></div>
    <address class="company-details">
      <div class="legal">
        ©Brisk Lending LLC.<br>
        NMLS #5093374<br>
        4716 Harlow Avenue #204,<br>
        Boulder, CO 80305<br>
        Not available in all states
      </div>
      <div class="contact-line">
        <svg viewBox="0 0 12 12" aria-hidden="true"><path fill="var(--teal)" d="M1 4c0-2 2-3 5-3s5 1 5 3v1H8V4H4v1H1zM3 6h6l1.5 5h-9z"/></svg>
        800.437.5068
      </div>
      <div class="contact-line">
        <svg viewBox="0 0 12 12" aria-hidden="true"><rect x="0.5" y="2" width="11" height="8" fill="var(--teal)"/><path d="M0.5 2l5.5 4.5L11.5 2" fill="none" stroke="#ffffff" stroke-width="1"/></svg>
        help@brisklending-example.com
      </div>
    </address>
  </header>

  <section class="letter-body">
    <p class="salutation">Dear customer,</p>
    <p>Lorem ipsum dolor sit amet, consectetur adipisicing elit, sed do eiusmod tempor incididunt ut labore et dolore magna aliqua. Ut enim ad minim veniam, quis nostrud exercitation ullamco laboris nisi ut aliquip ex ea commodo consequat. Duis aute irure dolor in reprehenderit in voluptate velit esse cillum dolore eu fugiat nulla pariatur. Excepteur sint occaecat cupidatat non proident, sunt in culpa qui officia deserunt mollit anim id est laborum.</p>
    <p>Lorem ipsum dolor sit amet, consectetur adipisicing elit, sed do eiusmod tempor incididunt ut labore et dolore magna aliqua. Ut enim ad minim veniam, quis nostrud exercitation ullamco laboris nisi ut aliquip ex ea commodo consequat. Duis aute irure dolor in reprehenderit in voluptate velit esse cillum dolore eu fugiat nulla pariatur. Excepteur sint occaecat cupidatat non proident, sunt in culpa qui officia deserunt mollit anim id est laborum.</p>
    <p>Lorem ipsum dolor sit amet, consectetur adipisicing elit, sed do eiusmod tempor incididunt ut labore et dolore magna aliqua. Ut enim ad minim veniam, quis nostrud exercitation ullamco laboris nisi ut aliquip ex ea commodo consequat. Duis aute irure dolor in reprehenderit in voluptate velit esse cillum dolore eu fugiat nulla pariatur. Excepteur sint occaecat cupidatat non proident, sunt in culpa qui officia deserunt mollit anim id est laborum.</p>
    <p>Lorem ipsum dolor sit amet, consectetur adipisicing elit, sed do eiusmod tempor incididunt ut labore et dolore magna aliqua. Ut enim ad minim veniam, quis nostrud exercitation ullamco laboris nisi ut aliquip ex ea commodo consequat. Duis aute irure dolor in reprehenderit.</p>
    <p class="salutation">Yours Sincerely,</p>
  </section>

  <div class="signature" role="img" aria-label="Handwritten signature"></div>

  <svg class="housing-badge" viewBox="0 0 106 102" role="img" aria-label="Equal housing badge">
    <rect x="8" y="12" width="90" height="86" fill="var(--mark)"/>
  </svg>

  <svg class="footer-band" viewBox="0 0 803 27" aria-hidden="true">
    <polygon points="0,9 522,9 510,27 0,27" fill="var(--navy)"/>
    <polygon points="518,27 536,0 803,0 803,27" fill="var(--teal)"/>
  </svg>
  <div class="website">www.brisklending-example.com</div>
</main>
</body>
</html>
```